Corvane Holdings , new business card design

investment firm with corporate clients . need double sided business card , vertical and horizontal options ,logo must be clear. prefer pantone colors only and sharp design. website also www.corvane-example.ae

Khalid Bin Rashed
Managing Director
Tel. +971 4 000 3829
Mobile +971 50 000 4172
khalid@corvane-example.ae
Palm Crest Tower, officw 18-B07, Qasr Gardens, Dubai

Contact Information for Business Card

Khalid Bin Rashed
Managing Director

Font styles to use
Serif

Colors

Designer to choose colors to be used in the design.

```html
<!DOCTYPE html>
<html lang="en">
<head>
<meta charset="utf-8">
<title>Corvane Holdings – Business Card 90 × 50 Horizontal</title>
<link href="https://fonts.googleapis.com/css2?family=Alegreya+Sans+SC:wght@500;700&family=Didact+Gothic&display=swap" rel="stylesheet">
<style>
  :root {
    --stage-light: #f1f1f1;
    --stage-dark: #b4b4b4;
    --floor: #7d7d7d;
    --ink: #111111;
    --card: #ffffff;
    --slate: #4a4a4a;
    --navy: #0d2a5c;
    --label: #1a1a1a;
    --name: #4b4b4b;
    --logo-on-dark: #d4d4d4;
    --on-slate: #ffffff;
  }
  html, body {
    margin: 0;
    width: 1200px;
    height: 694px;
    overflow: hidden;
  }
  body {
    position: relative;
    background: radial-gradient(ellipse at 50% 52%, var(--stage-light) 0%, #dcdcdc 45%, var(--stage-dark) 100%);
    font-family: "Didact Gothic", sans-serif;
    color: var(--label);
  }
  .sheet-title, .side-label {
    position: absolute;
    margin: 0;
    font-weight: 400;
    transform: translateX(-50%);
    white-space: nowrap;
  }
  .sheet-title { left: 605px; top: 76px; font-size: 25px; }
  .side-label { font-size: 19px; }
  .side-label--front { left: 281px; top: 128px; }
  .side-label--back { left: 905px; top: 143px; }

  .card {
    position: absolute;
    width: 568px;
    height: 315px;
    background: var(--card);
    box-shadow: 4px 5px 6px rgba(0,0,0,0.35);
    overflow: hidden;
  }
  .card--front { left: 29px; top: 172px; }
  .card--back { left: 615px; top: 174px; border: 1px solid #9a9a9a; box-sizing: border-box; }

  .wordmark {
    position: absolute;
    left: 0;
    width: 100%;
    text-align: center;
    font-family: "Didact Gothic", sans-serif;
    font-weight: 400;
    line-height: 1;
    color: var(--ink);
  }
  .wordmark__main { display: block; font-size: 64px; letter-spacing: 0.3em; padding-left: 0.3em; }
  .wordmark__sub { display: block; font-size: 22px; letter-spacing: 0.95em; padding-left: 0.95em; margin-top: 12px; }
  .card--front .wordmark { top: 32px; }

  .holder {
    position: absolute;
    left: 0; width: 100%;
    top: 144px;
    text-align: center;
    font-family: "Alegreya Sans SC", sans-serif;
    color: var(--name);
  }
  .holder__name { margin: 0; font-size: 25px; font-weight: 500; letter-spacing: 0.03em; line-height: 1.05; }
  .holder__name b { font-weight: 700; }
  .holder__role { margin: 1px 0 0; font-size: 20px; font-weight: 500; letter-spacing: 0.04em; line-height: 1.05; }

  .rule-navy { position: absolute; left: 0; top: 202px; width: 100%; height: 4px; background: var(--navy); }
  .contact-band {
    position: absolute; left: 0; top: 209px; width: 100%; bottom: 0;
    background: var(--slate);
    color: var(--on-slate);
    text-align: center;
    font-size: 16.5px;
    line-height: 19.2px;
    padding-top: 4px;
    box-sizing: border-box;
  }
  .contact-band p { margin: 0; }

  .back-header { position: absolute; left: 0; top: 0; width: 100%; height: 114px; background: var(--slate); }
  .card--back .wordmark { top: 12px; color: var(--logo-on-dark); }
  .card--back .wordmark__main { font-size: 58px; }
  .card--back .wordmark__sub { font-size: 19px; margin-top: 10px; }
  .services {
    position: absolute; left: 0; width: 100%; top: 180px;
    text-align: center; margin: 0; font-size: 19px; color: var(--ink);
  }
  .floor { position: absolute; left: 0; bottom: 0; }
</style>
</head>
<body>
  <h1 class="sheet-title">90 X 50 Horizontal</h1>
  <p class="side-label side-label--front">Front</p>
  <p class="side-label side-label--back">Back</p>

  <section class="card card--front" aria-label="Card front">
    <div class="wordmark">
      <span class="wordmark__main">CORVANE</span>
      <span class="wordmark__sub">HOLDINGS</span>
    </div>
    <div class="holder">
      <p class="holder__name"><b>Khalid</b> Bin Rashed</p>
      <p class="holder__role">Managing Director</p>
    </div>
    <div class="rule-navy"></div>
    <div class="contact-band">
      <p>Tel. +971 4 000 3829</p>
      <p>Mobile +971 50 000 4172</p>
      <p>khalid@corvane-example.ae</p>
      <p>www.corvane-example.ae</p>
      <p>Palm Crest Tower, officw 18-B07, Qasr Gardens, Dubai</p>
    </div>
  </section>

  <section class="card card--back" aria-label="Card back">
    <div class="back-header"></div>
    <div class="wordmark">
      <span class="wordmark__main">CORVANE</span>
      <span class="wordmark__sub">HOLDINGS</span>
    </div>
    <p class="services">Your services description here</p>
  </section>

  <svg class="floor" width="1200" height="24" viewBox="0 0 1200 24" aria-hidden="true">
    <path d="M8 2 Q600 -6 1192 2 L1192 24 L8 24 Z" fill="var(--floor)"/>
  </svg>
</body>
</html>
```